Bramblewood Poolworks llc Brochure

We need a creative and colorful "Tri-Fold brochure for our swimming pool remodel and construction company. Bramblewood Poolworks llc. In Atlanta Ga. See our website for ideas, content, and photos. We will edit text and photos after just make sure it is Adobe program file. Www.tarnvellapools.com | I couldn't work the sliders yesterday, please check the brief again. Thank you.

Target Market(s)

High end homeowners in metro Atlanta Georgia usa

Industry/Entity Type

Construction

Font styles to use
Serif

Colors
000000
33a6d7
00a990
f37122
ffffff

Requirements
Must have
• Clean colorful. Creative.
Nice to have
• Use more neutral colors to make the pool photos "pop".
Should not have
• Too many Primary colors in the pallet.

```html
<!DOCTYPE html>
<html lang="en">
<head>
<meta charset="utf-8">
<title>Bramblewood Poolworks llc Tri-Fold Brochure</title>
<link href="https://fonts.googleapis.com/css2?family=Roboto+Condensed:wght@400;700&display=swap" rel="stylesheet">
<style>
  :root {
    --teal: #33b6c9;
    --teal-deep: #1f9fb4;
    --green: #6dbb3f;
    --green-light: #8fcc4f;
    --ink: #3a3a3a;
    --paper: #ffffff;
    --stage: #f2f2f2;
    --brand-blue: #2369b3;
  }
  * { box-sizing: border-box; margin: 0; padding: 0; }
  html, body { width: 1200px; height: 863px; overflow: hidden; background: var(--stage); }
  body { font-family: "Roboto Condensed", sans-serif; color: var(--ink); position: relative; }

  .spread { position: absolute; left: 40px; top: 110px; width: 810px; height: 640px; display: flex; background: var(--paper); box-shadow: 0 6px 24px rgba(0,0,0,.15); }
  .panel { position: relative; width: 270px; height: 640px; overflow: hidden; background: var(--paper); }
  .panel + .panel { border-left: 1px solid #e4e4e4; }
  .bottom-strip { position: absolute; left: 0; right: 0; bottom: 0; height: 14px; background: var(--teal); }

  .panel-title { background: var(--green); color: var(--paper); font-weight: 700; font-size: 20px; letter-spacing: .3px; padding: 12px 16px 8px; }
  .panel-lead { background: var(--teal); color: var(--paper); font-size: 12.5px; line-height: 1.25; padding: 8px 16px 10px; }
  .body-copy { padding: 12px 18px 0; font-size: 8.6px; line-height: 1.35; text-align: justify; }
  .body-copy p { margin-bottom: 8px; }
  .body-copy .caps { text-transform: uppercase; }

  .photo { position: absolute; }
  .photo-evening { left: 0; bottom: 14px; width: 270px; height: 150px; background: linear-gradient(160deg, #2d3a2a 0%, #4a6a6d 45%, #8a7a62 100%); clip-path: path("M0 40 C 90 10, 180 0, 270 20 L270 150 L0 150 Z"); }
  .photo-patio { left: 0; top: 0; width: 270px; height: 300px; background: linear-gradient(170deg, #5d6a55 0%, #6fa9b2 38%, #b08f6c 62%, #8a6a4f 100%); }
  .photo-garden { left: 20px; top: 250px; width: 230px; height: 150px; background: linear-gradient(160deg, #2f4a2c 0%, #546b3f 55%, #7a6a52 100%); }
  .mid-copy { position: absolute; top: 312px; left: 0; right: 0; }
  .side-copy { position: absolute; top: 0; left: 0; right: 0; }

  .cover { position: absolute; left: 900px; top: 110px; width: 260px; height: 640px; background: var(--paper); overflow: hidden; box-shadow: 0 6px 24px rgba(0,0,0,.15); }
  .cover-photo { position: absolute; left: 0; top: 0; width: 260px; height: 300px; background: linear-gradient(165deg, #3b4f63 0%, #7a8c8f 35%, #3fb2d8 62%, #9b8468 100%); }
  .cover-waves { position: absolute; left: 0; top: 0; width: 260px; height: 640px; }
  .cover-tagline { position: absolute; left: 18px; right: 18px; top: 318px; color: var(--paper); font-size: 15px; line-height: 1.35; text-align: center; }
  .cover-tagline strong { font-weight: 700; }
  .brand { position: absolute; left: 0; right: 0; top: 540px; display: flex; align-items: center; justify-content: center; gap: 8px; }
  .brand-dot { width: 14px; height: 14px; border-radius: 50%; background: var(--teal); }
  .brand-name { font-weight: 700; font-size: 17px; color: var(--brand-blue); }
</style>
</head>
<body>
  <section class="spread" aria-label="Brochure inside spread">
    <article class="panel panel-philosophy">
      <h2 class="panel-title">ATLANTA POOL BUILDERS</h2>
      <p class="panel-lead">Our philosophy is based on the principles of taking a holistic approach to swimming pool design.</p>
      <div class="body-copy">
        <p>In many cases, pools are just forced into the yard without a focus on how the space will be used. We believe that the form should follow the function.</p>
        <p>Tarnvella Pools is dedicated to creative pool designs that are both optimized for the space and proper for the intended use. We find that this approach leads to a more creative finished product. Our landscape architects will help you choose the building materials that will define the finished look of the pool and landscape. The type of stone, plaster, decking materials, plants, trees and ground cover, play a significant part in how the finished product will look.</p>
        <p class="caps">Proactive communication is another key part of our philosophy.</p>
        <p>During the construction stage, we actively anticipate external factors that may impact the project and communicate them with our clients as needed to avoid unnecessary delays. We work closely with our clients during all stages of the project.</p>
        <p>Most of our clients will only build one swimming pool in their lifetimes and we believe that building a pool should be a pleasant experience. Our friendly and highly experienced staff provides our clients with the necessary information and services to help you keep up the pool after completion.</p>
        <p>Our pools feature the latest technology from Corvane, Halstrom, Stonefleck and more. Photos by Tarnvella Pools – All rights reserved.</p>
      </div>
      <div class="photo photo-evening" role="img" aria-label="Photo: pool and paver patio lit at dusk among trees"></div>
      <div class="bottom-strip"></div>
    </article>

    <article class="panel panel-natural">
      <div class="photo photo-patio" role="img" aria-label="Photo: blue pool and paver patio framed by curtains and a patio chair"></div>
      <div class="body-copy mid-copy">
        <p>Natural Pools Natural pools are designed to have a natural look and feel. Tarnvella Pools specializes in Natural Pools. This natural pool features a shelf entry, a spa and a Pavecrest Paver Patio. On this project, landscaping was added to soften the natural stone on the swimming pool and create a beautiful natural environment. All new landscaping including Cyprus trees were added to give privacy on either side of the property. Several large trees had</p>
        <p>Atlanta Pool Contractors, Tarnvella Pools, is your One Stop Source for Outdoor Living As Atlanta Pool Contractors over 30 years of experience in this field, we are dedicated to creating the highest quality outdoor living spaces. We specialize in custom pools and spas with an emphasis on quality and customer service. Tarnvella Pools will supply all of your outdoor living needs. We work with you to create unique, intuitive and functional designs that</p>
      </div>
      <div class="bottom-strip"></div>
    </article>

    <article class="panel panel-living">
      <div class="body-copy side-copy">
        <p>Outdoor Living Spaces should maximize the use of available space. This project was probably one of our biggest challenges. It features a (42 x 26) freeform pool, outdoor fireplace and a massive faux boulder swim-in grotto. Inside the grotto is a full size spa, a flat screen outdoor TV with surround sound, plenty of wet and dry walking room to spare as you walk out of the water and into the shade.</p>
      </div>
      <div class="photo photo-garden" role="img" aria-label="Photo: wooded garden seating area beside the pool"></div>
      <div class="bottom-strip"></div>
    </article>
  </section>

  <section class="cover" aria-label="Brochure front cover">
    <div class="cover-photo" role="img" aria-label="Photo: lit blue pool with waterfall grotto and timber pavilion at dusk"></div>
    <svg class="cover-waves" viewBox="0 0 260 640" aria-hidden="true">
      <path d="M0 290 C 80 260, 180 240, 260 200 L260 480 C 180 455, 90 450, 0 470 Z" fill="var(--green)"/>
      <path d="M0 300 C 90 272, 180 252, 260 214" stroke="var(--teal)" stroke-width="6" fill="none"/>
      <path d="M0 420 C 90 395, 170 400, 260 430" stroke="var(--green-light)" stroke-width="5" fill="none" opacity=".8"/>
      <path d="M0 470 C 90 450, 180 455, 260 480 L260 496 C 180 472, 90 468, 0 488 Z" fill="#d9d9d9"/>
      <path d="M0 500 C 90 488, 180 492, 260 500 L260 520 L0 520 Z" fill="var(--teal)"/>
      <rect x="0" y="626" width="260" height="14" fill="var(--teal)"/>
    </svg>
    <p class="cover-tagline"><strong>Atlanta Pool Builders</strong> with over <strong>30-years</strong> of experience in this field, we are dedicated to <strong>building the very</strong> highest quality <strong>outdoor living spaces.</strong></p>
    <div class="brand">
      <span class="brand-dot"></span>
      <span class="brand-name">Bramblewood Poolworks llc</span>
    </div>
  </section>
</body>
</html>
```